Buch-/E-Book-Cover
Zielgruppe
Wir verkaufen Trainings und vermitteln über unser Buch ein erstes vertieftes Wissen zum Thema Vermögensaufbau.
Aufgabenstellung
Es soll schlicht und schön sein, Angelehnt an Tall coin short coin, bzw. an Schau hin und bleib Klug von Bartholo Fenwick.
Wir benötigen die AI, etc Dateien und die fertigen Dateien für Velmora.de Lumora sowie Velmora.de Books (ehemals Printvale) mit fertigem Cover.
Vorgaben von Velmora.de über die Homepage. Anbei ein Beispiel (wegen Velmora.de Buchnummer etc) Abstände, Buchrücken etc.
Buch ca. 150 Seiten
https://www.velmora-beispiel.de/Gaertner-bleiben-heute-Zeichen-guten/dp/7392058164 Front und Backcover kann man sich da ansehen.
Der Buchtitel ist 'Baue Kredite und bleib frei' - - Lassen Sie uns freundschaftlich in entspannter Atmosphäre über Immobilien sprechen (der nebentitel so klein wie bei Tall Coin - Short Coin)
Rücktitel: Bitte zuerst Platzhalter.
Ich bitte um 5x8 inch, also wie DIN A 5, wir nehmen cremefarbenes Papier denke ich. Die Seitenzahl kann ich auf die Seite noch nicht sagen, wir haben aber 75 Din A4 Seiten, sprich nach Formatierung eher 160-165 Din A5. WErde ich Ihnen final nach dem Gewinn sagen.
Versuchen Sie mich mal aus dem einen Bild raus zu schneiden, und dass dann mit einem Layer über das cover zu legen.
2-3 Versionen wäre gut, mit 2-3 Bildern. Buchrücken ein kleines Bild von mir.
Seite vom Buch: Titel nochmal.

```html
<!DOCTYPE html>
<html lang="de">
<head>
<meta charset="utf-8">
<title>Baue Kredite und bleib frei – Coverentwürfe</title>
<link href="https://fonts.googleapis.com/css2?family=Lato:wght@400;700;900&display=swap" rel="stylesheet">
<style>
  :root {
    --page: #ffffff;
    --rule: #c9c9c9;
    --navy-1: #0b1430;
    --navy-2: #1c3768;
    --blue: #0a8fd8;
    --violet-1: #1b1033;
    --violet-2: #3a2160;
    --plum-1: #1a0c24;
    --plum-2: #5a1450;
    --magenta: #c0237e;
    --yellow: #f7b51b;
    --white: #ffffff;
    --ink: #1a1a1a;
    --suit-1: #2f2620;
    --suit-2: #5a4a40;
  }
  * { margin: 0; padding: 0; box-sizing: border-box; }
  html, body { width: 1200px; height: 1200px; overflow: hidden; background: var(--page); }
  body { position: relative; font-family: "Lato", sans-serif; }

  .rule { position: absolute; height: 1px; background: var(--rule); }

  .wrap {
    position: absolute; width: 578px; height: 446px;
    transform: scale(0.625); transform-origin: top left;
    overflow: hidden; color: var(--white);
    box-shadow: 2px 3px 6px rgba(0,0,0,.25);
  }
  .wrap--blue { background: radial-gradient(ellipse at 70% 30%, var(--navy-2), var(--navy-1) 70%); }
  .wrap--violet { background: linear-gradient(135deg, var(--violet-1), var(--violet-2) 60%, var(--violet-1)); }
  .wrap--plum { background: linear-gradient(150deg, var(--plum-1) 20%, var(--plum-2) 55%, var(--plum-1) 85%); }

  .band-stripe { position: absolute; transform-origin: left top; }

  .back { position: absolute; left: 0; top: 0; width: 276px; height: 446px; }
  .back-title { position: absolute; left: 0; width: 276px; top: 34px; text-align: center; font-weight: 900; line-height: 1; }
  .back-title .big { font-size: 18px; display: block; }
  .back-title .und { font-size: 9px; font-weight: 700; display: block; color: var(--white); }
  .back-blurb { position: absolute; left: 46px; top: 100px; width: 178px; font-size: 5.2px; line-height: 6.6px; text-align: justify; }
  .back-blurb p { margin-bottom: 6px; }
  .author { position: absolute; left: 46px; width: 178px; display: flex; gap: 12px; }
  .author-photo { width: 45px; height: 54px; flex: none; background: linear-gradient(180deg, #d9dde3, #8a8f99); }
  .author-text { font-size: 5.2px; line-height: 6.6px; text-align: justify; }
  .author-text b { font-weight: 900; }
  .barcode-box { position: absolute; top: 365px; width: 111px; height: 66px; background: var(--white); color: var(--ink); font-size: 7px; font-weight: 700; line-height: 8.5px; display: flex; align-items: center; justify-content: center; text-align: center; }

  .spine { position: absolute; top: 0; left: 276px; width: 28px; height: 446px; }
  .spine-title, .spine-author { position: absolute; left: 0; width: 28px; writing-mode: vertical-rl; transform: rotate(180deg); display: flex; align-items: center; justify-content: center; font-weight: 900; white-space: nowrap; }
  .spine-title { top: 80px; height: 220px; font-size: 11px; }
  .spine-title .und { font-size: 6px; font-weight: 700; margin: 3px 0; }
  .spine-author { top: 355px; height: 70px; font-size: 6px; }

  .front { position: absolute; left: 304px; top: 0; width: 274px; height: 446px; }
  .portrait { position: absolute; background: linear-gradient(180deg, var(--suit-2), var(--suit-1) 55%, #1a1512); border-radius: 40% 40% 6px 6px / 18% 18% 6px 6px; }
  .header { position: absolute; font-size: 10px; line-height: 12px; }
  .header b { font-weight: 900; }
  .title { position: absolute; font-weight: 900; line-height: 0.92; }
  .title .und { display: block; font-size: 15px; font-weight: 700; line-height: 1.2; }
  .title .line { display: block; }
  .tag { position: absolute; font-weight: 700; font-size: 11.5px; text-align: center; }
  .sub { position: absolute; font-size: 10px; line-height: 11.5px; text-align: center; }
  .badge { position: absolute; width: 80px; height: 80px; border-radius: 50%; background: var(--yellow); color: var(--plum-1); font-size: 6.6px; font-weight: 700; line-height: 7.6px; display: flex; align-items: center; justify-content: center; text-align: center; padding: 10px; }

  .accent-blue { color: var(--blue); }
  .accent-yellow { color: var(--yellow); }
</style>
</head>
<body>

<!-- Version 1: blau -->
<section class="wrap wrap--blue" style="left:259px; top:44px;">
  <div class="back">
    <h2 class="back-title"><span class="big accent-blue">BAUE KREDITE</span><span class="und">und</span><span class="big">BLEIB FREI</span></h2>
    <div class="back-blurb">
      <p>Klingt das für Sie nach einem Widerspruch? Dann kennen Sie den ImmobilienAdvisor Koray Morvan noch nicht. Schritt für Schritt berichtet er von seinem erstaunlichen Werdegang vom Lehrer zum Investor. Erfahren Sie, wie Sie Ihr erstes Objekt finden und sicher finanzieren. Praxisnah, ehrlich und verständlich erklärt er, was Sie wissen müssen – und werden Sie selbst zum Investor.</p>
      <p>Ein Denkanstoß gefällig? Bei heutigen Zinsen und gleichzeitiger Inflation können Sie zusehen, wie Ihre Kredite mit jedem Tag schrumpfen.</p>
      <p>Praxisrelevant, authentisch und auf Augenhöhe mit seinen Lesern bietet Ihnen der ImmobilienAdvisor einen neuen Weg in ein unabhängiges Leben. Fangen Sie gleich damit an!</p>
    </div>
    <div class="author" style="top:250px;">
      <div class="author-photo" role="img" aria-label="Kleines Porträtfoto des Autors"></div>
      <p class="author-text"><b>Über den Autor:</b> Koray Morvan war viele Jahre Lehrer, bevor er mit Immobilien begann. Heute berät er Einsteiger und zeigt ihnen, wie ein solider Vermögensaufbau gelingt, ruhig und ohne Hektik.</p>
    </div>
    <div class="barcode-box" style="left:153px;">Barcode<br>Location &amp; Size</div>
  </div>
  <div class="spine">
    <div class="spine-title"><span class="accent-blue">BAUE KREDITE</span><span class="und">&nbsp;und&nbsp;</span><span>BLEIB FREI</span></div>
    <div class="spine-author">KORAY MORVAN</div>
  </div>
  <div class="front">
    <div class="portrait" role="img" aria-label="Freigestelltes Foto des Autors im dunklen Anzug mit weißem Hemd" style="left:92px; top:22px; width:150px; height:424px;"></div>
    <p class="header" style="right:20px; top:14px;"><b>KORAY MORVAN –</b> DER IMMOBILIENADVISOR</p>
    <h1 class="title" style="left:0; width:274px; top:180px; text-align:center; font-size:40px;">
      <span class="line accent-blue">BAUE</span><span class="line accent-blue">KREDITE</span><span class="und">und</span><span class="line">BLEIB</span><span class="line">FREI</span>
    </h1>
    <p class="tag" style="left:21px; width:233px; top:360px; height:22px; line-height:22px; background:var(--blue);">GESPRÄCHE ÜBER IMMOBILIEN</p>
    <p class="sub" style="left:10px; width:254px; top:390px;">Lassen Sie uns unter Freunden in entspannter<br>Atmosphäre über Immobilien sprechen</p>
  </div>
</section>

<div class="rule" style="left:75px; top:350px; width:1074px;"></div>

<!-- Version 2: violett -->
<section class="wrap wrap--violet" style="left:778px; top:400px;">
  <div class="back">
    <h2 class="back-title"><span class="big accent-yellow">BAUE KREDITE</span><span class="und">und</span><span class="big">BLEIB FREI</span></h2>
    <div class="back-blurb">
      <p>Hier steht später der Klappentext zum Buch. Er beschreibt kurz den Inhalt, nennt die wichtigsten Themen und weckt die Neugier der Leser auf die Gespräche über Immobilien und Vermögen.</p>
      <p>Ein zweiter Absatz folgt an dieser Stelle und ergänzt den Text um weitere Gedanken, Beispiele und einen kurzen Ausblick auf die Kapitel.</p>
    </div>
    <div class="author" style="top:217px;">
      <div class="author-photo" role="img" aria-label="Kleines Porträtfoto des Autors"></div>
      <p class="author-text"><b>Über den Autor:</b> Koray Morvan war viele Jahre Lehrer, bevor er mit Immobilien begann. Heute berät er Einsteiger und zeigt ihnen, wie ein solider Vermögensaufbau gelingt, ruhig und ohne Hektik.</p>
    </div>
    <div class="barcode-box" style="left:153px;">Barcode<br>Location &amp; Size</div>
  </div>
  <div class="spine">
    <div class="spine-title"><span class="accent-yellow">BAUE KREDITE</span><span class="und">&nbsp;und&nbsp;</span><span>BLEIB FREI</span></div>
    <div class="spine-author">KORAY MORVAN</div>
  </div>
  <div class="front">
    <div class="portrait" role="img" aria-label="Freigestelltes Foto des Autors im dunklen Anzug mit weißem Hemd" style="left:100px; top:6px; width:150px; height:440px;"></div>
    <p class="header" style="left:20px; top:22px;"><b>KORAY MORVAN –</b><br>Der ImmobilienAdvisor</p>
    <h1 class="title" style="left:0; width:274px; top:160px; text-align:center; font-size:40px;">
      <span class="line accent-yellow">BAUE</span><span class="line accent-yellow">KREDITE</span><span class="und">und</span><span class="line">BLEIB</span><span class="line">FREI</span>
    </h1>
    <p class="tag" style="left:21px; width:233px; top:345px; height:22px; line-height:22px; background:var(--yellow); color:var(--violet-1);">GESPRÄCHE ÜBER IMMOBILIEN</p>
    <p class="sub" style="left:10px; width:254px; top:380px;">Lassen Sie uns unter Freunden in entspannter<br>Atmosphäre über Immobilien sprechen</p>
  </div>
</section>

<div class="rule" style="left:77px; top:712px; width:1053px;"></div>

<!-- Version 3: pflaume -->
<section class="wrap wrap--plum" style="left:251px; top:809px;">
  <div class="band-stripe" style="left:-40px; top:420px; width:720px; height:26px; background:var(--magenta); opacity:.55; transform:rotate(-30deg);"></div>
  <div class="back">
    <h2 class="back-title"><span class="big accent-yellow">BAUE KREDITE</span><span class="und">und</span><span class="big">BLEIB FREI</span></h2>
    <div class="back-blurb">
      <p>Hier steht später der Klappentext zum Buch. Er beschreibt kurz den Inhalt, nennt die wichtigsten Themen und weckt die Neugier der Leser auf die Gespräche über Immobilien und Vermögen.</p>
      <p>Ein zweiter Absatz folgt an dieser Stelle und ergänzt den Text um weitere Gedanken, Beispiele und einen kurzen Ausblick auf die Kapitel.</p>
    </div>
    <div class="author" style="top:217px;">
      <div class="author-photo" role="img" aria-label="Kleines Porträtfoto des Autors"></div>
      <p class="author-text"><b>Über den Autor:</b> Koray Morvan war viele Jahre Lehrer, bevor er mit Immobilien begann. Heute berät er Einsteiger und zeigt ihnen, wie ein solider Vermögensaufbau gelingt, ruhig und ohne Hektik.</p>
    </div>
    <div class="barcode-box" style="left:152px;">Barcode<br>Location &amp; Size</div>
  </div>
  <div class="spine">
    <div class="spine-title"><span class="accent-yellow">BAUE KREDITE</span><span class="und">&nbsp;und&nbsp;</span><span>BLEIB FREI</span></div>
    <div class="spine-author">KORAY MORVAN</div>
  </div>
  <div class="front">
    <div class="portrait" role="img" aria-label="Freigestelltes Foto des Autors im dunklen Anzug, Hand in der Tasche" style="left:0; top:4px; width:150px; height:442px;"></div>
    <p class="header" style="right:20px; top:20px; text-align:right;"><b class="accent-yellow">KORAY MORVAN –</b><br>DER IMMOBILIENADVISOR</p>
    <h1 class="title" style="right:21px; top:136px; text-align:right; font-size:38px;">
      <span class="line">BAUE</span><span class="line">KREDITE</span><span class="und accent-yellow">und</span><span class="line accent-yellow">BLEIB</span><span class="line accent-yellow">FREI</span>
    </h1>
    <p class="tag" style="right:21px; top:318px; font-size:10px; font-weight:400;">GESPRÄCHE ÜBER IMMOBILIEN</p>
    <p class="badge" style="left:172px; top:341px;">Lassen Sie uns unter Freunden in entspannter Atmosphäre über Immobilien sprechen</p>
  </div>
</section>

<div class="rule" style="left:77px; top:1114px; width:1053px;"></div>

</body>
</html>
```